Stationary

We have designed a new logo and business care.
It is now time for stationary.
We are a financial planning firm and are looking for something more formal that show the strength of our firm.
Please include our tag line; Integrity - Vision -Diligence.
I have uploaded a PDF of our current stationary - but - you are under no obligation to design anything like it.
Thx
Marta

```html
<!DOCTYPE html>
<html lang="en">
<head>
<meta charset="utf-8">
<title>Summit Harbor Group – Stationery</title>
<link href="https://fonts.googleapis.com/css2?family=Montserrat:wght@400;600&display=swap" rel="stylesheet">
<style>
  :root {
    --brand-blue: #2b3a91;
    --edge-grey: #6e6e6e;
    --paper: #ffffff;
    --backdrop: #e9ebee;
    --text-grey: #4a4a4a;
  }
  * { margin: 0; padding: 0; box-sizing: border-box; }
  html, body { width: 1200px; height: 872px; overflow: hidden; }
  body {
    position: relative;
    background: var(--backdrop);
    font-family: "Montserrat", sans-serif;
  }
  .letterhead {
    position: absolute; left: 58px; top: 68px;
    width: 568px; height: 736px;
    background: var(--paper);
    overflow: hidden;
  }
  .brand-name { color: var(--brand-blue); font-weight: 400; white-space: nowrap; }
  .tagline {
    font-size: 7px; letter-spacing: 4.4px; color: var(--text-grey);
    font-weight: 600; white-space: nowrap;
  }
  .letterhead .brand { position: absolute; left: 22px; top: 72px; }
  .letterhead .brand-name { font-size: 16px; margin-bottom: 4px; }
  .footer-band { position: absolute; left: 0; bottom: 0; width: 568px; height: 100px; }
  .contact {
    position: absolute; text-align: right; color: var(--brand-blue);
    font-size: 9.5px; line-height: 11.5px;
  }
  .contact .gap { height: 6px; }
  .contact svg { width: 7px; height: 7px; margin-left: 4px; vertical-align: -1px; fill: var(--brand-blue); }
  .letterhead .contact { right: 22px; bottom: 20px; }

  .card {
    position: absolute; left: 681px; width: 393px; height: 224px; overflow: hidden;
  }
  .card-front { top: 200px; background: var(--brand-blue); display: flex; align-items: center; justify-content: center; }
  .card-front .brand-name { color: var(--paper); font-size: 34px; }
  .card-back { top: 448px; background: var(--brand-blue); }
  .card-back svg.sweep { position: absolute; inset: 0; }
  .card-back .brand { position: absolute; left: 19px; top: 56px; }
  .card-back .brand-name { color: var(--paper); font-size: 11.5px; margin-bottom: 3px; }
  .card-back .tagline { color: var(--paper); font-size: 5px; letter-spacing: 3.4px; }
  .holder { position: absolute; right: 24px; top: 122px; text-align: right; }
  .holder-name { color: var(--brand-blue); font-weight: 600; font-size: 13px; }
  .holder-role { color: var(--text-grey); font-size: 9px; }
  .card-back .contact { right: 24px; top: 160px; color: var(--text-grey); font-size: 9.5px; line-height: 12px; }
</style>
</head>
<body>

<section class="letterhead">
  <div class="brand">
    <div class="brand-name">Summit Harbor Group</div>
    <div class="tagline">Clarity Trust Purpose</div>
  </div>
  <svg class="footer-band" viewBox="0 0 568 100" preserveAspectRatio="none">
    <rect width="568" height="100" fill="var(--brand-blue)"/>
    <path d="M124,100 C240,38 410,6 568,0 L568,100 Z" fill="var(--edge-grey)"/>
    <path d="M136,100 C250,42 415,8 568,1 L568,100 Z" fill="var(--paper)"/>
  </svg>
  <div class="contact">
    <div>(555) 014-2287<svg viewBox="0 0 10 10"><path d="M2,0.5 L4,0.5 L4.6,3 L3.3,3.8 Q4.3,6 6.2,6.8 L7,5.5 L9.5,6.1 L9.5,8.2 Q9,9.6 7.6,9.5 Q1,8.5 0.5,2.2 Q0.6,0.7 2,0.5 Z"/></svg></div>
    <div>(555) 014-2289<svg viewBox="0 0 10 10"><rect x="2.5" y="0.5" width="5" height="3"/><rect x="0.5" y="3.5" width="9" height="4" rx="1"/><rect x="2.5" y="7" width="5" height="2.5"/></svg></div>
    <div class="gap"></div>
    <div>2270 N, Larkfield</div>
    <div>St., Bellmont, WA 99001</div>
  </div>
</section>

<section class="card card-front">
  <div class="brand-name">Summit Harbor</div>
</section>

<section class="card card-back">
  <svg class="sweep" viewBox="0 0 393 224" preserveAspectRatio="none">
    <path d="M78,224 C100,110 250,20 393,0 L393,224 Z" fill="var(--edge-grey)"/>
    <path d="M88,224 C110,114 255,24 393,2 L393,224 Z" fill="var(--paper)"/>
    <path d="M393,112 L388,112 Q380,112 380,120 L380,204 Q380,212 388,212 L393,212 Z" fill="var(--brand-blue)"/>
  </svg>
  <div class="brand">
    <div class="brand-name">Summit Harbor Group</div>
    <div class="tagline">Clarity Trust Purpose</div>
  </div>
  <div class="holder">
    <div class="holder-name">Owen Carter</div>
    <div class="holder-role">Director</div>
  </div>
  <div class="contact">
    <div>(555) 014-2287<svg viewBox="0 0 10 10"><path d="M2,0.5 L4,0.5 L4.6,3 L3.3,3.8 Q4.3,6 6.2,6.8 L7,5.5 L9.5,6.1 L9.5,8.2 Q9,9.6 7.6,9.5 Q1,8.5 0.5,2.2 Q0.6,0.7 2,0.5 Z"/></svg></div>
    <div>(555) 014-2289<svg viewBox="0 0 10 10"><rect x="2.5" y="0.5" width="5" height="3"/><rect x="0.5" y="3.5" width="9" height="4" rx="1"/><rect x="2.5" y="7" width="5" height="2.5"/></svg></div>
    <div class="gap"></div>
    <div>2270 N, Larkfield</div>
    <div>St., Bellmont, WA 99001</div>
  </div>
</section>

</body>
</html>
```